Over 100 ladies will be traveling to Ocean City, MD for a Women's Retreat Conference. This flyer is for advertisement. This flyer is to circulate for registrations as well as to post on social media. Theme is Holy Spirit fire. I have attached a photo. All the information in the attachment should be included on the flyer. Information should be clearly readable end eye catching.

Target Market(s)

Church ladies

Industry/Entity Type

Religious

Font styles to use
Sans Serif

Colors

Designer to choose colors to be used in the design.

Requirements
Must have
• Title: Tidewell Womens Retreat 2019 "FIRE"
• All components in attachments

```html
<!DOCTYPE html>
<html lang="en">
<head>
<meta charset="utf-8">
<title>Tidewell Womens Retreat 2019 – FIRE</title>
<link rel="stylesheet" href="https://fonts.googleapis.com/css2?family=Cinzel:wght@400;700&family=Lato:ital,wght@0,400;0,700;0,900;1,400;1,700&family=Montserrat:wght@900&family=Oswald:wght@500;700&display=swap">
<style>
  :root {
    --ink: #0b0605;
    --white: #ffffff;
    --paper: #fbf8f5;
    --orange: #f0821a;
    --orange-deep: #e4500c;
    --flame: #ff7a12;
    --ember: #9c1c04;
    --yellow: #ffd23a;
    --text-dark: #222222;
  }
  * { box-sizing: border-box; margin: 0; padding: 0; }
  html, body { width: 902px; height: 1200px; overflow: hidden; background: #ffffff; }
  .flyer {
    position: relative;
    width: 902px;
    height: 1200px;
    overflow: hidden;
    font-family: "Lato", sans-serif;
    color: var(--text-dark);
  }
  .backdrop { position: absolute; inset: 0; }
  .title {
    position: absolute; top: 62px; left: 0; width: 100%;
    text-align: center;
    font-family: "Cinzel", serif; font-weight: 400;
    font-size: 92px; letter-spacing: 2px; line-height: 1;
    color: var(--white);
  }
  .title .lead { font-size: 108px; }
  .subtitle {
    position: absolute; top: 164px; left: 0; width: 100%;
    text-align: center;
    font-family: "Cinzel", serif; font-weight: 400;
    font-size: 44px; line-height: 1; color: var(--orange);
  }
  .subtitle .lead { font-size: 52px; }
  .theme { position: absolute; top: 236px; left: 150px; }

  .speaker { position: absolute; left: 40px; width: 290px; text-align: center; }
  .speaker .portrait {
    width: 166px; height: 166px; margin: 0 auto;
    border-radius: 50%;
    border: 4px solid var(--ink);
    box-shadow: 0 0 0 4px var(--white);
  }
  .speaker .role { margin-top: 14px; font-size: 15px; font-weight: 700; color: var(--white); line-height: 1.25; }
  .speaker .name { font-size: 16px; font-weight: 700; color: var(--text-dark); line-height: 1.25; }
  .host { top: 426px; }
  .speaker-one { top: 658px; }
  .speaker-two { top: 890px; }

  .venue { position: absolute; left: 374px; top: 580px; display: flex; gap: 8px; }
  .venue .pin { width: 36px; height: 36px; flex: none; }
  .venue-name { font-size: 16.5px; font-weight: 700; color: var(--orange); line-height: 1.22; text-transform: uppercase; }
  .venue-address { font-size: 14px; color: var(--text-dark); line-height: 1.3; }

  .venue-photo { position: absolute; }
  .venue-photo.stair { left: 600px; top: 472px; width: 108px; height: 108px; border-radius: 50%; border: 4px solid var(--white); }
  .venue-photo.facade { left: 650px; top: 557px; width: 208px; height: 122px; border-radius: 10px; }
  .venue-photo.room { left: 765px; top: 655px; width: 106px; height: 106px; border-radius: 50%; border: 4px solid var(--white); }

  .included { position: absolute; left: 382px; top: 735px; width: 500px; }
  .included h2 {
    font-family: "Cinzel", serif; font-weight: 400; font-size: 20px;
    color: var(--orange-deep); letter-spacing: 1px; margin-bottom: 12px;
  }
  .included ul { list-style: none; display: grid; grid-template-columns: 270px 230px; row-gap: 9px; }
  .included li { display: flex; align-items: center; gap: 9px; font-size: 14px; font-style: italic; color: var(--text-dark); }
  .included li:nth-child(1) { grid-column: 1; grid-row: 1; }
  .included li:nth-child(2) { grid-column: 1; grid-row: 2; }
  .included li:nth-child(3) { grid-column: 2; grid-row: 1; }
  .included li:nth-child(4) { grid-column: 2; grid-row: 2; }
  .tick { width: 16px; height: 16px; flex: none; }

  .pricing { position: absolute; left: 400px; top: 880px; width: 470px; text-align: center; color: var(--white); }
  .price { font-family: "Oswald", sans-serif; font-weight: 700; font-size: 44px; line-height: 1; letter-spacing: 0.5px; }
  .price .label { color: var(--orange); margin-right: 12px; }
  .occupancy { font-size: 17px; font-weight: 400; margin-top: 10px; }
  .terms { margin: 12px auto 0; width: 380px; font-size: 10.5px; font-style: italic; line-height: 1.3; }

  .contact { position: absolute; left: 400px; top: 1100px; width: 420px; text-align: center; color: var(--ink); font-size: 13px; font-weight: 700; }
  .contact-lines { display: flex; justify-content: center; gap: 36px; margin-top: 12px; color: var(--white); font-weight: 400; font-size: 14px; }
  .contact-lines span, .web { display: inline-flex; align-items: center; gap: 7px; }
  .contact-lines svg, .web svg { width: 15px; height: 15px; }
  .web { margin-top: 12px; color: var(--white); font-weight: 700; font-size: 14px; }
  .web .url { font-weight: 400; }
</style>
</head>
<body>
<main class="flyer">
  <svg class="backdrop" width="902" height="1200" viewBox="0 0 902 1200" aria-hidden="false">
    <defs>
      <radialGradient id="topFire" cx="0.1" cy="0.55" r="0.7">
        <stop offset="0" stop-color="#f7a526"/>
        <stop offset="0.35" stop-color="#b8380a"/>
        <stop offset="0.7" stop-color="#3a0c04"/>
        <stop offset="1" stop-color="#0b0605"/>
      </radialGradient>
      <linearGradient id="panelFire" x1="0" y1="0" x2="1" y2="0">
        <stop offset="0" stop-color="#ffd23a"/>
        <stop offset="0.3" stop-color="#f79a1c"/>
        <stop offset="0.7" stop-color="#ea5e0e"/>
        <stop offset="1" stop-color="#e4500c"/>
      </linearGradient>
      <radialGradient id="emberBowl" cx="0.7" cy="0.45" r="0.7">
        <stop offset="0" stop-color="#ff8a1e"/>
        <stop offset="0.35" stop-color="#a8280a"/>
        <stop offset="0.75" stop-color="#1c0704"/>
        <stop offset="1" stop-color="#0b0605"/>
      </radialGradient>
      <linearGradient id="band" x1="0" y1="0" x2="0" y2="1">
        <stop offset="0" stop-color="#ff8a1a"/>
        <stop offset="1" stop-color="#e9480a"/>
      </linearGradient>
    </defs>
    <rect width="902" height="1200" fill="var(--ink)"/>
    <rect width="902" height="560" fill="url(#topFire)" role="img" aria-label="Photo of swirling flames across the top"/>
    <path d="M0,405 C120,372 250,368 340,408 C330,418 380,436 430,470 C560,540 720,566 902,528 L902,1200 L0,1200 Z" fill="var(--paper)"/>
    <path d="M0,432 C150,420 290,440 350,472 C290,560 250,700 292,880 C318,1000 338,1110 356,1200 L0,1200 Z" fill="url(#panelFire)" role="img" aria-label="Flame photo fading from yellow to orange"/>
    <ellipse cx="635" cy="1000" rx="250" ry="158" fill="url(#emberBowl)" role="img" aria-label="Flames rising against a dark background"/>
    <path d="M300,1200 L300,1110 C380,1095 430,1080 470,1084 C520,1070 560,1082 620,1070 C690,1062 740,1080 800,1060 C850,1050 880,1055 902,1040 L902,1200 Z" fill="url(#band)"/>
  </svg>

  <h1 class="title"><span class="lead">T</span>IDEWELL</h1>
  <p class="subtitle"><span class="lead">W</span>OMENS <span class="lead">R</span>ETREAT, 2019</p>

  <svg class="theme" width="600" height="170" viewBox="0 0 600 170" role="img" aria-label="Theme: FIRE">
    <defs>
      <linearGradient id="wordFire" x1="0" y1="0" x2="1" y2="1">
        <stop offset="0" stop-color="#ffb52e"/>
        <stop offset="0.4" stop-color="#e2450c"/>
        <stop offset="0.75" stop-color="#7a1204"/>
        <stop offset="1" stop-color="#f08a1c"/>
      </linearGradient>
    </defs>
    <text x="10" y="90" font-family="Cinzel, serif" font-size="110" fill="var(--orange)">“</text>
    <text x="300" y="155" text-anchor="middle" font-family="Montserrat, sans-serif" font-weight="900" font-size="168" letter-spacing="6" fill="url(#wordFire)" stroke="var(--white)" stroke-width="5" paint-order="stroke">FIRE</text>
    <text x="545" y="90" font-family="Cinzel, serif" font-size="110" fill="var(--orange)">”</text>
  </svg>

  <section class="speaker host">
    <div class="portrait" role="img" aria-label="Portrait photo of the retreat host" style="background:radial-gradient(circle at 50% 40%, #c98d6a, #7a3a2a 60%, #f2e7e0 61%)"></div>
    <p class="role">Retreat Host:</p>
    <p class="name">Apostle Miriam Calder</p>
  </section>
  <section class="speaker speaker-one">
    <div class="portrait" role="img" aria-label="Portrait photo of a retreat speaker" style="background:radial-gradient(circle at 50% 45%, #5a3322, #1d1412 60%, #c8c8c8 61%)"></div>
    <p class="role">Retreat Speaker</p>
    <p class="name">Pastor Loretta Haynes - Orlando, Florida</p>
  </section>
  <section class="speaker speaker-two">
    <div class="portrait" role="img" aria-label="Portrait photo of a retreat speaker" style="background:radial-gradient(circle at 50% 45%, #6b3d28, #151112 60%, #f3f3f3 61%)"></div>
    <p class="role">Retreat Speaker</p>
    <p class="name">Pastor Denise Whitfield - GLCM<br>- Waldorf, Md.</p>
  </section>

  <div class="venue-photo stair" role="img" aria-label="Photo of the hotel lobby staircase" style="background:linear-gradient(160deg,#f4d98a,#c89a52 55%,#e9e2d2)"></div>
  <div class="venue-photo facade" role="img" aria-label="Night photo of the hotel building" style="background:linear-gradient(180deg,#1f3a6a 0%,#2b4f86 45%,#e0a67a 46%,#b9775a 85%,#314a2c 100%)"></div>
  <div class="venue-photo room" role="img" aria-label="Photo of a hotel guest room" style="background:linear-gradient(150deg,#cfe0ea,#6d9fb8 55%,#f1f1ee)"></div>

  <section class="venue">
    <svg class="pin" viewBox="0 0 36 36" aria-hidden="true">
      <circle cx="18" cy="18" r="16" fill="none" stroke="#2f6fb0" stroke-width="1.5"/>
      <path d="M18 8a6.5 6.5 0 0 0-6.5 6.5c0 5 6.5 12.5 6.5 12.5s6.5-7.5 6.5-12.5A6.5 6.5 0 0 0 18 8z" fill="var(--orange)"/>
      <circle cx="18" cy="14.5" r="2.6" fill="var(--white)"/>
    </svg>
    <div>
      <p class="venue-name">Seacrest Harbor Hotel<br>&amp; Suites</p>
      <p class="venue-address">1450 Seabreeze Ave.<br>Ocean City, Maryland 21842</p>
    </div>
  </section>

  <section class="included">
    <h2>Included:</h2>
    <ul>
      <li><svg class="tick" viewBox="0 0 16 16"><circle cx="8" cy="8" r="6.5" fill="none" stroke="var(--orange-deep)" stroke-width="1.6"/><path d="M4.8 8.2l2.2 2.2 5.5-5.8" fill="none" stroke="var(--orange-deep)" stroke-width="2"/></svg>All Retreat Sessions</li>
      <li><svg class="tick" viewBox="0 0 16 16"><circle cx="8" cy="8" r="6.5" fill="none" stroke="var(--orange-deep)" stroke-width="1.6"/><path d="M4.8 8.2l2.2 2.2 5.5-5.8" fill="none" stroke="var(--orange-deep)" stroke-width="2"/></svg>2 Nights Hotel Accommodations</li>
      <li><svg class="tick" viewBox="0 0 16 16"><circle cx="8" cy="8" r="6.5" fill="none" stroke="var(--orange-deep)" stroke-width="1.6"/><path d="M4.8 8.2l2.2 2.2 5.5-5.8" fill="none" stroke="var(--orange-deep)" stroke-width="2"/></svg>1 Hot Lunch Buffet</li>
      <li><svg class="tick" viewBox="0 0 16 16"><circle cx="8" cy="8" r="6.5" fill="none" stroke="var(--orange-deep)" stroke-width="1.6"/><path d="M4.8 8.2l2.2 2.2 5.5-5.8" fill="none" stroke="var(--orange-deep)" stroke-width="2"/></svg>1 Full Hot American Breakfast</li>
    </ul>
  </section>

  <section class="pricing">
    <p class="price"><span class="label">COST:</span>$295</p>
    <p class="occupancy">*Based on double occupancy</p>
    <p class="terms">**ALL deposits/registrations are NON-refundable and NON-transferable. Your entire registration is due by October 1, 2019. Please submit your desired roommate's name at the time of registration. If you do not choose a roommate one will be assigned to you unless you have registered for a private room.</p>
  </section>

  <section class="contact">
    <p>Please contact Renee via email or phone for more information.</p>
    <div class="contact-lines">
      <span><svg viewBox="0 0 16 16"><rect x="1.5" y="3.5" width="13" height="9" fill="none" stroke="currentColor" stroke-width="1.4"/><path d="M1.5 3.5l6.5 5 6.5-5" fill="none" stroke="currentColor" stroke-width="1.4"/></svg>renee@caldergraceministries.org</span>
      <span><svg viewBox="0 0 16 16"><circle cx="8" cy="8" r="7" fill="none" stroke="currentColor" stroke-width="1.2"/><path d="M5.2 4.2l1.6-.4.9 2-1 .8a5 5 0 0 0 2.6 2.6l.8-1 2 .9-.4 1.6c-3.6.3-6.8-2.9-6.5-6.5z" fill="currentColor"/></svg>240-555-0148</span>
    </div>
    <p class="web">Visit us today! <svg viewBox="0 0 16 16"><circle cx="8" cy="8" r="6.5" fill="none" stroke="currentColor" stroke-width="1.3"/><ellipse cx="8" cy="8" rx="2.8" ry="6.5" fill="none" stroke="currentColor" stroke-width="1.1"/><path d="M1.5 8h13" stroke="currentColor" stroke-width="1.1"/></svg><span class="url">tidewell2019.events.example</span></p>
  </section>
</main>
</body>
</html>
```